Dietitian clinic needs a business card design

We need a business card design for a new dietitian group based in Singapore called "Brightpath and Bloom". We provide expert, personalised nutrition care to support a wide range of health needs, from chronic conditions to mindful eating. Our team also offers consulting, speaking, and tailored solutions for healthcare providers, organisations, and food services.

Target Market(s)

Adults

Industry/Entity Type

Healthcare

Contact Information for Business Card

Name, position, contact number, email, website address, our logo

Requirements
Nice to have
• Clean, professional but welcoming look

```html
<!DOCTYPE html>
<html lang="en">
<head>
<meta charset="utf-8">
<title>Brightpath and Bloom – Business Card</title>
<link href="https://fonts.googleapis.com/css2?family=Playfair+Display:ital,wght@0,600;0,700;1,400&family=Poppins:wght@300;400&display=swap" rel="stylesheet">
<style>
  :root {
    --bg: #e4e4e4;
    --card: #ffffff;
    --navy: #1f5468;
    --blush: #dba1a1;
    --pink: #f2898c;
    --pink-light: #f8b7b6;
    --teal: #45b3ad;
    --teal-light: #8fd1cc;
    --icon: #e58b88;
  }
  * { margin: 0; padding: 0; box-sizing: border-box; }
  html, body { width: 1200px; height: 1200px; overflow: hidden; }
  body { background: var(--bg); position: relative; font-family: "Poppins", sans-serif; }

  .card {
    position: absolute; left: 181px; width: 838px; height: 477px;
    background: var(--card); overflow: hidden;
  }
  .card--front { top: 91px; }
  .card--back { top: 631px; }
  .card__waves { position: absolute; inset: 0; width: 100%; height: 100%; }

  .brand { position: absolute; display: flex; align-items: center; }
  .brand__dot { border-radius: 50%; flex: none; }
  .brand__name {
    font-family: "Playfair Display", serif; font-weight: 700;
    line-height: 0.9; letter-spacing: -1px;
  }

  .card--front .brand { left: 118px; top: 150px; gap: 40px; }
  .card--front .brand__dot { width: 110px; height: 110px; background: var(--navy); }
  .card--front .brand__name { color: var(--navy); font-size: 66px; }

  .intro {
    position: absolute; left: 150px; width: 538px; top: 318px;
    text-align: center; color: var(--navy);
    font-size: 17.5px; font-weight: 300; line-height: 27px;
  }

  .card--back .brand { left: 40px; top: 40px; flex-direction: column; gap: 22px; width: 360px; }
  .card--back .brand__dot { width: 96px; height: 96px; background: var(--blush); }
  .card--back .brand__name { color: var(--blush); font-size: 56px; text-align: center; }

  .person { position: absolute; left: 475px; top: 165px; color: var(--navy); }
  .person__name { font-family: "Playfair Display", serif; font-weight: 600; font-size: 27px; }
  .person__role { display: flex; align-items: center; margin-top: 2px; }
  .person__title { font-family: "Playfair Display", serif; font-style: italic; font-size: 25px; }
  .person__creds {
    font-size: 17px; margin-left: 10px; padding-left: 10px;
    border-left: 1.5px solid var(--navy); line-height: 22px;
  }

  .contact { position: absolute; left: 480px; top: 323px; list-style: none; color: var(--navy); font-size: 19px; }
  .contact li { display: flex; align-items: center; gap: 7px; height: 24.5px; }
  .contact svg { width: 17px; height: 17px; flex: none; }
</style>
</head>
<body>

<section class="card card--front">
  <svg class="card__waves" viewBox="0 0 838 477" preserveAspectRatio="none" aria-hidden="true">
    <defs>
      <linearGradient id="pinkFront" x1="0" y1="0" x2="1" y2="0">
        <stop offset="0" stop-color="var(--pink-light)"/>
        <stop offset="1" stop-color="var(--pink)"/>
      </linearGradient>
      <linearGradient id="tealFront" x1="0" y1="1" x2="1" y2="0">
        <stop offset="0" stop-color="var(--teal-light)"/>
        <stop offset="1" stop-color="var(--teal)"/>
      </linearGradient>
    </defs>
    <path d="M0,0 H455 C380,10 300,40 220,58 C150,72 60,70 0,62 Z" fill="url(#pinkFront)"/>
    <path d="M0,40 C90,45 180,35 260,18 C320,6 380,0 420,0" fill="none" stroke="#fff" stroke-width="2" opacity="0.7"/>
    <path d="M160,477 C300,458 430,468 560,428 C680,392 760,330 838,312 V477 Z" fill="url(#tealFront)"/>
    <path d="M180,470 C330,452 450,460 580,440 C690,420 770,380 838,350" fill="none" stroke="#fff" stroke-width="3"/>
    <path d="M420,477 C560,470 680,450 838,400" fill="none" stroke="var(--teal)" stroke-width="2" opacity="0.5"/>
  </svg>

  <div class="brand">
    <span class="brand__dot"></span>
    <span class="brand__name">brightpath<br>&amp; bloom</span>
  </div>

  <p class="intro">Brightpath &amp; Bloom – Nutrition is a practice with years of experience in top institutions. We bring that expertise into every session, offering compassionate nutrition care tailored to your goals.</p>
</section>

<section class="card card--back">
  <svg class="card__waves" viewBox="0 0 838 477" preserveAspectRatio="none" aria-hidden="true">
    <defs>
      <linearGradient id="pinkBack" x1="0" y1="0" x2="1" y2="0">
        <stop offset="0" stop-color="var(--pink)"/>
        <stop offset="1" stop-color="var(--pink-light)"/>
      </linearGradient>
      <linearGradient id="tealBack" x1="0" y1="0" x2="1" y2="1">
        <stop offset="0" stop-color="var(--teal-light)"/>
        <stop offset="0.6" stop-color="var(--teal)"/>
      </linearGradient>
    </defs>
    <path d="M390,0 H838 V75 C760,76 700,62 620,42 C540,22 460,10 390,0 Z" fill="url(#pinkBack)"/>
    <path d="M420,0 C520,12 600,30 680,48 C740,60 790,62 838,58" fill="none" stroke="#fff" stroke-width="2" opacity="0.8"/>
    <path d="M0,290 C120,300 200,360 300,420 C380,460 520,470 730,477 H0 Z" fill="url(#tealBack)"/>
    <path d="M0,300 C130,310 210,370 310,425 C400,462 540,468 700,474" fill="none" stroke="#fff" stroke-width="3"/>
    <path d="M0,340 C110,360 190,400 280,440 C330,462 380,472 430,477" fill="none" stroke="#fff" stroke-width="1.5" opacity="0.5"/>
  </svg>

  <div class="brand">
    <span class="brand__dot"></span>
    <span class="brand__name">brightpath<br>&amp; bloom</span>
  </div>

  <div class="person">
    <h1 class="person__name">Dr. Mariam Haleem</h1>
    <div class="person__role">
      <span class="person__title">Principal Dietitian</span>
      <span class="person__creds">RD, PhD, ADS</span>
    </div>
  </div>

  <ul class="contact">
    <li>
      <svg viewBox="0 0 24 24" aria-hidden="true"><path d="M6.6 10.8a15.2 15.2 0 0 0 6.6 6.6l2.2-2.2c.3-.3.7-.4 1-.2 1.1.4 2.3.6 3.6.6.6 0 1 .4 1 1V20c0 .6-.4 1-1 1C10.6 21 3 13.4 3 4c0-.6.4-1 1-1h3.5c.6 0 1 .4 1 1 0 1.3.2 2.5.6 3.6.1.3 0 .7-.2 1z" fill="var(--icon)"/></svg>
      +(65) 8000 1234
    </li>
    <li>
      <svg viewBox="0 0 24 24" aria-hidden="true"><rect x="2" y="5" width="20" height="14" rx="1" fill="var(--icon)"/><path d="M2 6l10 7 10-7" fill="none" stroke="#fff" stroke-width="1.6"/></svg>
      hello@brightpathandbloom.com
    </li>
    <li>
      <svg viewBox="0 0 24 24" aria-hidden="true"><circle cx="12" cy="12" r="9" fill="none" stroke="var(--icon)" stroke-width="2"/><ellipse cx="12" cy="12" rx="4" ry="9" fill="none" stroke="var(--icon)" stroke-width="1.6"/><path d="M3 12h18M5 7.5h14M5 16.5h14" stroke="var(--icon)" stroke-width="1.4"/></svg>
      brightpathandbloom.com
    </li>
  </ul>
</section>

</body>
</html>
```